"STRONG past SIXTY" fitness and nutritional reseller needs a Facebook page

"Strong past Sixty" is an independent reseller of corevista.example fitness videos (K42z, Overdrive, Iron Titan, etc.) and related equipment. We also resell corevista.example nutritional plans (30 week reset) and supplements like protein shakes (Blendvora). I am looking for a Facebook page that looks fun yet is professional. I would like the color scheme to include Blue, Teal, Gray, White to match a logo of similar colors.

Industry/Entity Type

Fitness

```html
<!DOCTYPE html>
<html lang="en">
<head>
<meta charset="utf-8">
<title>Strong past Sixty</title>
<link href="https://fonts.googleapis.com/css2?family=Roboto:wght@400;500;700&display=swap" rel="stylesheet">
<style>
:root{
  --navy:#1f4fa3;
  --navy-dark:#173f86;
  --teal:#19a3a8;
  --page:#eef0f3;
  --card:#ffffff;
  --line:#dde1e7;
  --text:#2d3540;
  --muted:#8a929c;
  --red:#e0413a;
}
*{box-sizing:border-box;margin:0;padding:0}
html,body{width:791px;height:1200px;overflow:hidden}
body{font-family:'Roboto',sans-serif;background:var(--page);color:var(--text);position:relative;font-size:7px}

.topbar{position:absolute;left:0;top:0;width:791px;height:40px;background:var(--navy)}
.brand{position:absolute;left:20px;top:10px;color:#fff;font-size:17px;font-weight:500}
.badge{position:absolute;top:7px;width:13px;height:9px;border-radius:3px;background:var(--red);color:#fff;font-size:6px;text-align:center;line-height:9px}
.search{position:absolute;left:237px;top:10px;width:262px;height:17px;background:#fff;border-radius:9px;padding-left:10px;color:var(--muted);font-size:7px;line-height:17px}
.nav{position:absolute;right:20px;top:14px;display:flex;gap:26px;color:#fff;font-size:7px;font-weight:500;letter-spacing:.3px}

.cover{position:absolute;left:45px;top:50px;width:700px;height:240px;background:linear-gradient(100deg,#cfd4da,#8b6f60 35%,#b9a598 60%,#e3e6ea)}
.cover-actions{position:absolute;right:10px;bottom:8px;display:flex;gap:4px}
.cover-actions span{background:#fff;border:1px solid var(--line);font-size:6px;padding:3px 7px;color:var(--text)}
.profile-bar{position:absolute;left:45px;top:290px;width:700px;height:40px;background:var(--card);border-bottom:1px solid var(--line)}
.avatar-big{position:absolute;left:55px;top:245px;width:60px;height:80px;border:3px solid #fff;background:linear-gradient(160deg,#6f5a52,#c8a491)}
.profile-name{position:absolute;left:80px;top:8px;font-size:7px;font-weight:700}
.profile-sub{position:absolute;left:80px;top:18px;font-size:6px;color:var(--muted)}
.tabs{position:absolute;right:20px;top:14px;display:flex;gap:26px;font-size:6.5px;color:var(--muted)}
.tabs .active{color:var(--text);font-weight:500;border-bottom:2px solid var(--navy);padding-bottom:8px}

.col{position:absolute;top:362px}
.col-left{left:45px;width:170px}
.col-mid{left:230px;width:330px}
.col-right{left:575px;width:170px}
.card{background:var(--card);border:1px solid var(--line);margin-bottom:14px}
.head{display:flex;gap:6px;padding:8px}
.thumb{width:26px;height:26px;flex:none;background:linear-gradient(135deg,#9c8274,#d9c4b6)}
.title{font-size:7.5px;font-weight:500}
.desc{font-size:5.5px;color:var(--muted);line-height:1.5;margin-top:2px}
.meta{font-size:5.5px;color:var(--muted);margin-top:3px}
.meta b{color:var(--teal);font-weight:500}
.actions{display:flex;justify-content:space-between;border-top:1px solid var(--line);padding:6px 8px;font-size:6px;color:var(--navy);font-weight:500}

.composer-tabs{display:flex;gap:14px;padding:7px 8px;border-bottom:1px solid var(--line);font-size:6px;color:var(--muted)}
.composer-input{padding:9px 8px;font-size:6px;color:var(--muted)}
.post-img{height:150px;margin:0 8px;background:linear-gradient(120deg,#2d2d2f,#6b5547 55%,#b89a82)}
.post-body{padding:8px}
.grid{display:grid;grid-template-columns:repeat(4,1fr);gap:3px;margin:0 8px;height:115px}
.grid div:nth-child(1){background:linear-gradient(#7a8da0,#c9a88f)}
.grid div:nth-child(2){background:linear-gradient(#7faa4e,#d9b85a)}
.grid div:nth-child(3){background:linear-gradient(#5b4a40,#a58772)}
.grid div:nth-child(4){background:linear-gradient(#c66b7c,#e2c5b8)}
.loader{position:absolute;left:385px;top:1075px;width:20px;height:20px}
.loader-text{position:absolute;left:380px;top:1098px;font-size:5.5px;color:var(--muted)}

.side-img{height:88px;background:linear-gradient(130deg,#3c3f45,#9c857a 60%,#d4d6da)}
.side-img.two{background:linear-gradient(130deg,#2a2a2c,#8a6a58)}
.side-img.three{background:linear-gradient(130deg,#d0d3d8,#c2707e 55%,#8d7666)}
.side-text{padding:7px 8px}

.footer{position:absolute;left:0;top:1140px;width:791px;height:60px;background:var(--navy-dark);color:#cfd9ee;font-size:6px;text-align:center;line-height:60px}
</style>
</head>
<body>

<header class="topbar">
  <div class="brand">Strong past Sixty</div>
  <span class="badge" style="left:150px">2</span>
  <span class="badge" style="left:168px">5</span>
  <div class="search">Search</div>
  <nav class="nav"><span>HOME</span><span>PROFILE</span><span>ACCOUNT ▾</span></nav>
</header>

<section class="cover" role="img" aria-label="Cover photo of a man lifting a barbell in a gym">
  <div class="cover-actions"><span>👍 Like</span><span>Follow</span><span>Share</span><span>•••</span></div>
</section>
<section class="profile-bar">
  <div class="profile-name">FITNESS &amp; NUTRITIONAL</div>
  <div class="profile-sub">Reseller</div>
  <div class="tabs"><span class="active">Timeline</span><span>About Us</span><span>Photos</span><span>Strong past Sixty</span><span>More ▾</span></div>
</section>
<div class="avatar-big" role="img" aria-label="Profile photo of a woman at the gym"></div>

<aside class="col col-left">
  <div class="card">
    <div class="head"><div class="thumb" role="img" aria-label="Workout photo"></div><div><div class="title">Fitness Videos</div><div class="desc">Home workouts and meal plans to keep you strong, steady and active every week.</div><div class="meta">5 hrs ago · <b>Like</b></div></div></div>
    <div class="actions"><span>Like</span><span>Comment</span><span>Share</span><span>12</span></div>
  </div>
  <div class="card">
    <div class="head"><div class="thumb" role="img" aria-label="Workout photo"></div><div><div class="title">Fitness Videos</div><div class="desc">Home workouts and meal plans to keep you strong, steady and active every week.</div><div class="meta">5 hrs ago · <b>Like</b></div></div></div>
    <div class="actions"><span>Like</span><span>Comment</span><span>Share</span><span>12</span></div>
  </div>
  <div class="card">
    <div class="head"><div class="thumb" role="img" aria-label="Workout photo"></div><div><div class="title">Fitness Videos</div><div class="desc">Home workouts and meal plans to keep you strong, steady and active every week.</div><div class="meta">5 hrs ago · <b>Like</b></div></div></div>
    <div class="actions"><span>Like</span><span>Comment</span><span>Share</span><span>12</span></div>
  </div>
  <div class="card">
    <div class="head"><div class="thumb" role="img" aria-label="Program photo"></div><div><div class="title">K42z</div><div class="desc">Ninety days of mixed strength and cardio training.</div></div></div>
    <div class="head"><div class="thumb" role="img" aria-label="Program photo"></div><div><div class="title">Overdrive</div><div class="desc">High energy cardio circuits you can do at home.</div></div></div>
    <div class="head"><div class="thumb" role="img" aria-label="Program photo"></div><div><div class="title">Iron Titan</div><div class="desc">Heavy lifting plan for serious muscle gains.</div></div></div>
  </div>
</aside>

<main class="col col-mid">
  <div class="card" style="margin-bottom:0">
    <div class="composer-tabs"><span>✎ Status</span><span>▣ Photos</span><span>➦ Share</span></div>
    <div class="composer-input">What's on your mind?</div>
  </div>
  <article class="card">
    <div class="head"><div class="thumb" role="img" aria-label="Page avatar"></div><div><div class="title">Strong past Sixty</div><div class="meta">10 hrs ago</div></div></div>
    <div class="post-img" role="img" aria-label="Muscular man holding a dumbbell"></div>
    <div class="post-body"><div class="title">K42z</div><div class="desc">A proven home program mixing weights, cardio and stretching. Join our group to start training with friends and get daily tips from coaches who have been there.</div></div>
    <div class="actions"><span>Like</span><span>Comment</span><span>Share</span><span>👍 12</span></div>
  </article>
  <article class="card">
    <div class="head"><div class="thumb" role="img" aria-label="Page avatar"></div><div><div class="title">Strong past Sixty</div><div class="meta">10 hrs ago</div></div></div>
    <div class="grid" role="img" aria-label="Four photos of training and healthy food"><div></div><div></div><div></div><div></div></div>
    <div class="post-body"><div class="title">Iron Titan</div><div class="desc">Build real size and strength with a structured lifting schedule. Pair it with a clean meal plan and a daily shake for steady progress.</div></div>
    <div class="actions"><span>Like</span><span>Comment</span><span>Share</span><span>👍 8</span></div>
  </article>
</main>

<svg class="loader" viewBox="0 0 20 20"><circle cx="10" cy="10" r="7" fill="none" stroke="#c9ced6" stroke-width="2" stroke-dasharray="3 2.5"/></svg>
<div class="loader-text">Loading</div>

<aside class="col col-right">
  <div class="card" style="margin-bottom:8px">
    <div class="side-img" role="img" aria-label="Woman exercising with weights"></div>
    <div class="side-text"><div class="title">K42z</div><div class="desc">Start today and feel stronger in weeks with guided daily workouts you can follow at home.</div></div>
  </div>
  <div class="card" style="margin-bottom:8px">
    <div class="side-img two" role="img" aria-label="Athlete training in a dark gym"></div>
  </div>
  <div class="card" style="margin-bottom:8px">
    <div class="side-img three" role="img" aria-label="Woman doing a floor workout"></div>
    <div class="side-text"><div class="desc">Simple moves for joints, balance and core, made for every fitness level.</div></div>
  </div>
  <div class="card">
    <div class="side-text"><div class="title">30 week reset</div><div class="desc">Portion control containers and easy recipes for lasting results.</div></div>
    <div class="actions"><span>Like</span><span>Comment</span><span>Share</span></div>
  </div>
</aside>

<footer class="footer">© Copy Rights 2015 Strong past Sixty All Rights Reserved</footer>

</body>
</html>
```